RPN FORMED

building services
decks
pergola
renovation
extensions
general building

Target Market(s)

middle to upper class

Industry/Entity Type

building

Contact Information for Business Card

my details 0438917264 tkbarrow47@mailvora.com BLD581047

Font styles to use
Serif

Colors
00AB8E
00BBA5
67D7C9
C6EFE9
E9F9F6

Requirements
Must have
• logo on the front and details on the back
Nice to have
• sharp and clean lines

```html
<!DOCTYPE html>
<html lang="en">
<head>
<meta charset="utf-8">
<title>RPN FORMED – Business Card</title>
<link rel="stylesheet" href="https://fonts.googleapis.com/css2?family=Libre+Baskerville:wght@700&family=Poppins:wght@300;400;600&family=Montserrat:wght@400&display=swap">
<style>
  :root {
    --teal: #41b59d;
    --teal-dark: #3aa88f;
    --teal-light: #67d7c9;
    --icon-bg: #8ee8d8;
    --ink: #111111;
    --canvas: #ececec;
    --card: #f3f3f3;
  }
  * { margin: 0; padding: 0; box-sizing: border-box; }
  html, body { width: 1200px; height: 2249px; overflow: hidden; }
  body { background: var(--canvas); position: relative; }

  .card {
    position: absolute;
    top: 704px;
    width: 480px;
    height: 840px;
    overflow: hidden;
    background: linear-gradient(135deg, #f7f7f7 0%, #ececec 30%, #f8f8f8 55%, #ebebeb 75%, #f5f5f5 100%);
    box-shadow: 0 3px 6px rgba(0,0,0,0.25);
  }
  .card--front { left: 72px; }
  .card--back { left: 638px; }

  .card__header { position: absolute; top: 0; left: 0; width: 480px; }

  .card__skyline {
    position: absolute;
    left: 0; bottom: 0;
    width: 480px; height: 111px;
    background: linear-gradient(180deg, var(--teal) 0%, var(--teal) 100%);
  }

  .wordmark {
    position: absolute;
    left: 0; width: 480px;
    text-align: center;
    font-family: "Libre Baskerville", serif;
    font-weight: 700;
    font-size: 50px;
    line-height: 1;
    color: var(--ink);
    letter-spacing: 1px;
  }
  .card--front .wordmark { top: 392px; }
  .card--back .wordmark { top: 125px; }

  .person {
    position: absolute; left: 0; width: 480px; text-align: center;
    font-family: "Poppins", sans-serif; line-height: 1;
  }
  .person__name { top: 244px; font-size: 52px; font-weight: 300; color: var(--ink); }
  .person__surname { font-weight: 600; color: var(--teal); }
  .person__licence { top: 300px; font-size: 26px; font-weight: 600; color: var(--ink); }
  .person__licence-prefix { color: var(--teal); }

  .contact__icon {
    position: absolute; left: 222px;
    width: 36px; height: 36px;
    background: var(--icon-bg);
  }
  .contact__icon svg { display: block; width: 36px; height: 36px; }
  .contact__text {
    position: absolute; left: 0; width: 480px; text-align: center;
    font-family: "Montserrat", sans-serif; font-size: 28px; line-height: 1;
    color: var(--ink);
  }
  .contact--phone .contact__icon { top: 388px; }
  .contact--phone .contact__text { top: 442px; font-size: 31px; }
  .contact--email .contact__icon { top: 494px; }
  .contact--email .contact__text { top: 546px; font-size: 26px; }
  .contact--web .contact__icon { top: 604px; }
  .contact--web .contact__text { top: 656px; }
</style>
</head>
<body>

  <section class="card card--front" aria-label="Card front">
    <svg class="card__header" width="480" height="182" viewBox="0 0 480 182">
      <polygon points="0,0 480,0 480,115 247,181 0,115" fill="var(--teal)"/>
    </svg>
    <h1 class="wordmark">RPN FORMED</h1>
    <div class="card__skyline" role="img" aria-label="Teal city skyline silhouette of buildings"></div>
  </section>

  <section class="card card--back" aria-label="Card back">
    <svg class="card__header" width="480" height="84" viewBox="0 0 480 84">
      <polygon points="0,0 480,0 480,17 248,82 0,17" fill="var(--teal)"/>
    </svg>
    <h2 class="wordmark">RPN FORMED</h2>

    <p class="person person__name">Tk <span class="person__surname">Barrow</span></p>
    <p class="person person__licence"><span class="person__licence-prefix">BLD</span>581047</p>

    <div class="contact contact--phone">
      <span class="contact__icon">
        <svg viewBox="0 0 36 36" aria-hidden="true">
          <path d="M11 9c1-1 2.5-1 3 0l2 4c.4.8 0 1.6-.6 2l-1.4 1c1 2.6 3 4.6 5.6 5.6l1-1.4c.4-.6 1.2-1 2-.6l4 2c1 .5 1 2 0 3l-2 2c-6 1-15-8-14-14z" fill="#111"/>
        </svg>
      </span>
      <p class="contact__text">0438917264</p>
    </div>

    <div class="contact contact--email">
      <span class="contact__icon">
        <svg viewBox="0 0 36 36" aria-hidden="true">
          <rect x="8" y="11" width="20" height="14" fill="#111"/>
          <polyline points="8,11 18,19 28,11" fill="none" stroke="#8ee8d8" stroke-width="1.6"/>
        </svg>
      </span>
      <p class="contact__text">tkbarrow47@mailvora.com</p>
    </div>

    <div class="contact contact--web">
      <span class="contact__icon">
        <svg viewBox="0 0 36 36" aria-hidden="true">
          <circle cx="18" cy="18" r="9" fill="#111"/>
          <g fill="none" stroke="#8ee8d8" stroke-width="1.2">
            <ellipse cx="18" cy="18" rx="4" ry="9"/>
            <line x1="9" y1="18" x2="27" y2="18"/>
            <line x1="11" y1="13.5" x2="25" y2="13.5"/>
            <line x1="11" y1="22.5" x2="25" y2="22.5"/>
          </g>
        </svg>
      </span>
      <p class="contact__text">www.rpnformed.com</p>
    </div>

    <div class="card__skyline" role="img" aria-label="Teal city skyline silhouette of buildings"></div>
  </section>

</body>
</html>
```